I need business cards for a company that will be an umbrella for many retail stores. I need them to be sleek and modern. I would like some white and black in the background of the card as these are the office colours the logo is attached.
Target Market(s)
worldwide
Industry/Entity Type
Business
Requirements
Must have
- traditional business card shape
Should not have
- too many colours
no swirly text

```html
<!DOCTYPE html>
<html lang="en">
<head>
<meta charset="utf-8">
<title>Navira General Trading – Business Card</title>
<link rel="stylesheet" href="https://fonts.googleapis.com/css2?family=Open+Sans:wght@400;700&display=swap">
<style>
  :root {
    --card-bg: #ffffff;
    --brand-navy: #173f8a;
    --text-blue: #1f4e9c;
    --rule-blue: #1b4a96;
    --accent-soft: #c3cce8;
  }
  * { margin: 0; padding: 0; box-sizing: border-box; }
  html, body {
    width: 1200px;
    height: 634px;
    overflow: hidden;
    background: var(--card-bg);
  }
  .card {
    position: relative;
    width: 1200px;
    height: 634px;
    background: var(--card-bg);
    font-family: "Open Sans", Tahoma, sans-serif;
  }
  .card__rules {
    position: absolute;
    inset: 0;
  }
  .brand__mark {
    position: absolute;
    left: 40px;
    top: 22px;
    width: 244px;
    height: 244px;
    border-radius: 50%;
    background: var(--accent-soft);
  }
  .brand {
    position: absolute;
    left: 313px;
    top: 208px;
    color: var(--brand-navy);
    font-weight: 700;
    font-size: 24px;
    line-height: 40px;
  }
  .brand__name { display: block; padding-left: 16px; }
  .owner {
    position: absolute;
    left: 313px;
    top: 316px;
    color: var(--brand-navy);
    font-weight: 700;
    font-size: 23px;
    line-height: 38px;
  }
  .contact {
    position: absolute;
    left: 313px;
    top: 471px;
    color: var(--text-blue);
    font-size: 21px;
    line-height: 41px;
  }
  .contact__row {
    display: grid;
    grid-template-columns: 324px auto;
  }
</style>
</head>
<body>
  <main class="card">
    <svg class="card__rules" width="1200" height="634" viewBox="0 0 1200 634" aria-hidden="true">
      <line x1="277" y1="289" x2="1183" y2="289" stroke="var(--rule-blue)" stroke-width="4"/>
      <line x1="268" y1="282" x2="268" y2="614" stroke="var(--rule-blue)" stroke-width="3"/>
    </svg>

    <span class="brand__mark" aria-hidden="true"></span>
    <div class="brand">
      <span class="brand__name">Navira</span>
      <span>General Trading</span>
    </div>

    <div class="owner">
      <p>Name of Business Owner</p>
      <p>Title of owner</p>
    </div>

    <div class="contact">
      <p class="contact__row"><span>Phone : 000.000.0000</span><span>Faxl: 000.000.0000</span></p>
      <p class="contact__row"><span>owner@navirastores.com</span><span>www.navirastores.com</span></p>
      <p>complete address of the Retail owner plus the P.O. Box number</p>
    </div>
  </main>
</body>
</html>
```